Web Site

Target Market(s)

CEOs and International Sales & Marketing Directors of International Companies who wish to expand their business reach to Dubai and the Middle East and are looking for a local professional partner to work with.

Requirements
Must have
• Creativity is key. We don't want the normal standard boxes of text and boxes of pics. Be as creative as you like.
Nice to have
• (This is only a suggestion, we welcome your creativity)
- The center of all pages could be large rotating pictures which display professional corporate men/women working in an office, images of Dubai, the UAE, skyscrapers of business towers in Dubai, ..etc.
- Images should reflect Dubai and the Arab World as a modern, fast-paced, growing modern market - Not Traditional)
Should not have
• Not so colorful, the fewer colors you use, the better.
Not Crammed or Busy
Not Traditional but modern

```html
<!DOCTYPE html>
<html lang="en">
<head>
<meta charset="utf-8">
<title>Alder Group – Employment &amp; Association</title>
<link rel="stylesheet" href="https://fonts.googleapis.com/css2?family=Arimo:wght@400;700&display=swap">
<style>
  :root {
    --ink: #222222;
    --heading: #333333;
    --body-text: #8c8c8c;
    --accent: #8b1a1a;
    --link: #5e0b0b;
    --nav-top: #8e8e8e;
    --nav-bottom: #5f5f5f;
    --nav-divider: #4a4a4a;
    --nav-highlight: #a6a6a6;
    --rule: #dddddd;
    --quote: #8c8c8c;
    --hero-from: #c4c1cc;
    --hero-to: #aeb0ab;
    --white: #ffffff;
  }
  * { box-sizing: border-box; margin: 0; padding: 0; }
  html, body {
    width: 1200px; height: 1051px; overflow: hidden;
    background: var(--white);
    font-family: "Arimo", Arial, sans-serif;
  }
  .page { position: relative; width: 1200px; height: 1051px; }

  /* Header */
  .brand {
    position: absolute; left: 121px; top: 36px;
    color: var(--ink); font-weight: 400; line-height: 1;
  }
  .brand-name { display: block; font-size: 50px; letter-spacing: -1px; }
  .brand-sub { display: block; font-size: 17px; letter-spacing: 13px; margin-top: 4px; padding-left: 2px; }

  .search {
    position: absolute; left: 868px; top: 86px; width: 214px; height: 27px;
    border: 1px solid #8f8f8f; border-radius: 5px; background: var(--white);
    display: flex; overflow: hidden;
  }
  .search-field { flex: 1; font-size: 14px; color: #8a8a8a; padding: 5px 10px; line-height: 16px; }
  .search-button {
    width: 45px; border-left: 1px solid #8f8f8f;
    display: flex; align-items: center; justify-content: center;
    background: linear-gradient(#ffffff, #e9e9e9);
  }

  /* Navigation */
  .main-nav {
    position: absolute; left: 121px; top: 143px; width: 961px; height: 41px;
    border-radius: 4px;
    background: linear-gradient(var(--nav-top), var(--nav-bottom));
    box-shadow: 0 2px 3px rgba(0,0,0,0.25);
    display: flex;
  }
  .nav-item {
    position: relative;
    color: var(--white); font-size: 16px; line-height: 41px; text-align: center;
    border-left: 1px solid var(--nav-highlight);
    border-right: 1px solid var(--nav-divider);
    white-space: nowrap;
  }
  .nav-item:first-child { border-left: none; }
  .nav-item:last-child { border-right: none; }
  .nav-item.is-active::before {
    content: ""; position: absolute; left: 50%; top: 0; transform: translateX(-50%);
    border-left: 10px solid transparent; border-right: 10px solid transparent;
    border-top: 9px solid var(--accent);
  }

  /* Slider */
  .hero {
    position: absolute; left: 146px; top: 234px; width: 910px; height: 348px;
    border-radius: 7px; overflow: hidden;
    background: linear-gradient(135deg, var(--hero-from), var(--hero-to));
  }
  .hero-shadow {
    position: absolute; left: 170px; top: 580px; width: 862px; height: 12px;
    background: radial-gradient(ellipse at top, rgba(0,0,0,0.22), rgba(0,0,0,0) 70%);
  }
  .hero-quote {
    position: absolute; right: 68px; top: 38px;
    color: var(--quote); font-size: 28px; font-weight: 700; line-height: 35px; text-align: right;
  }
  .hero-quote .mark { font-family: Georgia, serif; font-size: 40px; color: #9a9a9a; vertical-align: -4px; }
  .slider-arrow {
    position: absolute; top: 384px; width: 46px; height: 46px; border-radius: 50%;
    background: var(--white); border: 1px solid #d8d8d8;
    box-shadow: 0 1px 3px rgba(0,0,0,0.15);
    color: #333; font-size: 24px; line-height: 42px; text-align: center;
  }
  .slider-arrow.prev { left: 118px; }
  .slider-arrow.next { left: 1036px; }

  /* Content */
  .column { position: absolute; top: 631px; }
  .column-left { left: 118px; width: 396px; }
  .column-right { left: 601px; width: 456px; }
  .section-title { font-size: 19px; font-weight: 700; color: var(--heading); margin-bottom: 44px; }
  .sub-title { font-size: 16px; font-weight: 700; color: var(--heading); }
  .copy {
    font-size: 15px; line-height: 23.5px; color: var(--body-text);
    letter-spacing: 0.8px;
  }
  .column-left .copy { text-align: left; }
  .column-right .copy { text-align: justify; }
  .column-left .sub-title { margin-bottom: 31px; }
  .column-left .copy + .copy { margin-top: 37px; }
  .column-right .sub-title { margin-bottom: 39px; margin-top: 2px; }
  .column-right .copy + .copy { margin-top: 43px; }
  .email { color: var(--link); font-weight: 700; text-decoration: underline; letter-spacing: 1px; }
  .column-divider {
    position: absolute; left: 566px; top: 621px; width: 6px; height: 334px;
    background: linear-gradient(90deg, rgba(0,0,0,0.06), rgba(0,0,0,0));
    -webkit-mask: linear-gradient(transparent, #000 30%, #000 70%, transparent);
            mask: linear-gradient(transparent, #000 30%, #000 70%, transparent);
  }

  /* Footer */
  .site-footer {
    position: absolute; left: 0; top: 969px; width: 1200px; height: 82px;
    border-top: 1px solid var(--rule);
  }
  .copyright { position: absolute; left: 120px; top: 36px; font-size: 14px; color: #888; }
  .copyright .brand-mention { color: var(--accent); }
  .footer-link { position: absolute; right: 118px; top: 34px; font-size: 16px; color: #888; }
</style>
</head>
<body>
<div class="page">
  <header>
    <div class="brand">
      <span class="brand-name">ALDER</span>
      <span class="brand-sub">GROUP</span>
    </div>
    <div class="search">
      <span class="search-field">Search...</span>
      <span class="search-button">
        <svg width="20" height="18" viewBox="0 0 20 18" aria-hidden="true">
          <circle cx="7" cy="7" r="5" fill="none" stroke="#888" stroke-width="2"/>
          <line x1="11" y1="10.5" x2="17" y2="15" stroke="#888" stroke-width="3" stroke-linecap="round"/>
        </svg>
      </span>
    </div>
    <nav class="main-nav">
      <span class="nav-item" style="width:76px">Home</span>
      <span class="nav-item" style="width:142px">About the Group</span>
      <span class="nav-item" style="width:175px">Chairman's Message</span>
      <span class="nav-item" style="width:86px">Divisions</span>
      <span class="nav-item" style="width:155px">Group Companies</span>
      <span class="nav-item is-active" style="width:214px">Employment &amp; Association</span>
      <span class="nav-item" style="width:113px">Contact us</span>
    </nav>
  </header>

  <section class="slider">
    <div class="hero" role="img" aria-label="Photograph of a modern city skyline of towers along the waterfront with a yacht on the water">
      <p class="hero-quote"><span class="mark">“</span> Welcome to Alder Group<br>of Companies <span class="mark">”</span></p>
    </div>
    <div class="hero-shadow"></div>
    <span class="slider-arrow prev">&lt;</span>
    <span class="slider-arrow next">&gt;</span>
  </section>

  <main>
    <div class="column column-left">
      <h1 class="section-title">Employment &amp; Alliances :</h1>
      <h2 class="sub-title">Employment :</h2>
      <p class="copy">Are you goal oriented, motivated and looking for a challenging career with ALDER Group? ?</p>
      <p class="copy">For Employment opportunities with us, please contact us on <span class="email">info@aldergroup.com</span> and attach your CV with a recent photographand the position you are interested in.</p>
    </div>
    <div class="column-divider"></div>
    <div class="column column-right">
      <h2 class="sub-title">Alliances :</h2>
      <p class="copy">Are you a professional individual working with a professional reputable organization with long years of experience in a certain industry, looking to work with ALDER Group on an a strategic association basis?</p>
      <p class="copy">For Strategic Association opportunities with us, please contact us on <span class="email">info@aldergroup.com</span> and attach your CV with a recent photograph and how do you see working with the Group can be of benefit to us and to you.</p>
    </div>
  </main>

  <footer class="site-footer">
    <p class="copyright">Copyrights @ 2012 <span class="brand-mention">ALDER GROUP</span></p>
    <span class="footer-link">Contact us</span>
  </footer>
</div>
</body>
</html>
```